BrivaTrek Freight Services Business cards

Would like a very unique design catchy but professional for business cards. Please use log provided.Marlon WellsCeo and Founder TransCon Logistix Solutions1-888-913-3225mwells@tlsolutionsus.comwww.bfservicesco.com

```html
<!DOCTYPE html>
<html lang="en">
<head>
<meta charset="utf-8">
<title>BrivaTrek Freight Services – Business Cards</title>
<link rel="stylesheet" href="https://fonts.googleapis.com/css2?family=Marcellus+SC&family=Lato:wght@400;700&display=swap">
<style>
  :root {
    --stage: #3b3c40;
    --card: #1f2124;
    --blue: #1f74c4;
    --red: #e0242c;
    --card-w: 600px;
    --card-h: 343px;
  }
  * { box-sizing: border-box; margin: 0; padding: 0; }
  html, body { width: 1200px; height: 800px; overflow: hidden; }
  body {
    background: var(--stage);
    display: flex;
    flex-direction: column;
    align-items: center;
    justify-content: center;
    gap: 40px;
    font-family: "Lato", sans-serif;
  }
  .card {
    width: var(--card-w);
    height: var(--card-h);
    background: var(--card);
    position: relative;
    overflow: hidden;
    box-shadow: 0 12px 30px rgba(0,0,0,.45);
  }

  /* Front */
  .card--front { display: flex; align-items: center; justify-content: center; }
  .wordmark {
    display: flex; align-items: center; gap: 14px;
    font-family: "Marcellus SC", serif;
    color: var(--blue);
    font-size: 34px;
    letter-spacing: 1px;
  }
  .wordmark__square { width: 26px; height: 26px; background: var(--red); }

  /* Back */
  .card--back { display: flex; }
  .back__brand {
    width: 190px;
    position: relative;
    border-right: 2px solid var(--red);
  }
  .back__brand-name {
    position: absolute;
    left: 50%; top: 50%;
    transform: translate(-50%, -50%) rotate(90deg);
    white-space: nowrap;
    font-family: "Marcellus SC", serif;
    color: var(--blue);
    font-size: 24px;
    letter-spacing: 1px;
  }
  .back__details {
    flex: 1;
    padding: 46px 36px 0 32px;
  }
  .person__name {
    font-family: "Marcellus SC", serif;
    color: var(--blue);
    font-size: 26px;
    letter-spacing: 1px;
    line-height: 1;
  }
  .person__title { color: var(--red); font-size: 14px; margin-top: 4px; }
  .rule { height: 1px; background: var(--red); margin: 14px 0 12px; }
  .company__name {
    font-family: "Marcellus SC", serif;
    color: var(--blue);
    font-size: 19px;
    letter-spacing: .5px;
  }
  .company__address { color: var(--blue); font-size: 14px; line-height: 1.35; margin-top: 2px; }
  .contact { list-style: none; margin-top: 4px; }
  .contact__item {
    display: flex; align-items: center; gap: 10px;
    color: var(--blue); font-size: 14px; line-height: 1; margin-bottom: 9px;
  }
  .contact__icon { width: 18px; height: 18px; flex: none; }
  .contact__web-domain { color: var(--red); }
</style>
</head>
<body>

  <section class="card card--front" aria-label="Business card front">
    <div class="wordmark">
      <span class="wordmark__square"></span>
      <span class="wordmark__name">BrivaTrek Freight Services</span>
    </div>
  </section>

  <section class="card card--back" aria-label="Business card back">
    <div class="back__brand">
      <span class="back__brand-name">BrivaTrek Freight Services</span>
    </div>
    <div class="back__details">
      <p class="person__name">Dustin Harrow</p>
      <p class="person__title">Ceo and Founder</p>
      <div class="rule"></div>
      <p class="company__name">BrivaTrek Freight Services</p>
      <p class="company__address">2417 Calloway Ridge Rd,<br>Marston, GA 30582</p>
      <div class="rule"></div>
      <ul class="contact">
        <li class="contact__item">
          <svg class="contact__icon" viewBox="0 0 18 18" aria-hidden="true">
            <circle cx="9" cy="9" r="8" fill="none" stroke="#e0242c" stroke-width="1.6"/>
            <path d="M6 5.2c.4-.4 1-.4 1.3 0l.8 1.2c.2.4.1.8-.2 1l-.5.4c.4.9 1.1 1.6 2 2l.4-.5c.3-.3.7-.4 1-.2l1.2.8c.4.3.4.9 0 1.3l-.6.6c-2.6.5-6-2.9-5.6-5.6z" fill="#e0242c"/>
          </svg>
          <span>1-888-472-6081</span>
        </li>
        <li class="contact__item">
          <svg class="contact__icon" viewBox="0 0 18 18" aria-hidden="true">
            <circle cx="9" cy="9" r="8" fill="#e0242c"/>
            <rect x="4.8" y="6" width="8.4" height="6" fill="none" stroke="#1f2124" stroke-width="1.2"/>
            <path d="M4.8 6 9 9.3 13.2 6" fill="none" stroke="#1f2124" stroke-width="1.2"/>
          </svg>
          <span>dharrow@bfservicesco.com</span>
        </li>
        <li class="contact__item">
          <svg class="contact__icon" viewBox="0 0 18 18" aria-hidden="true">
            <circle cx="9" cy="9" r="8" fill="#e0242c"/>
            <circle cx="9" cy="9" r="4.2" fill="none" stroke="#1f2124" stroke-width="1.1"/>
            <path d="M4.8 9h8.4M9 4.8c-1.6 2.5-1.6 5.9 0 8.4M9 4.8c1.6 2.5 1.6 5.9 0 8.4" fill="none" stroke="#1f2124" stroke-width="1"/>
          </svg>
          <span>www.<span class="contact__web-domain">bfservicesco.com</span></span>
        </li>
      </ul>
    </div>
  </section>

</body>
</html>
```